Company providing Business Management Services needs modern business card

The business provides services like tender preparation, bank submissions, business health checks, financial and admin support. We want to portray 'Trust', 'Strength' and 'Support'.
2 styles of logo in various formats have been uploaded.
Looking for easy to understand, yet sophisticated and stand out from the crowd.

Target Market(s)

Small and Medium sized businesses

Industry/Entity Type

Business

Contact Information for Business Card

Name - Daniel Vesterby, Description - Manager, Phone - 0472 915 603, Email - danielvesterby@kpwholdingsgroup.example, Work description - Business Management Services.

Requirements
Must have
• Logo

```html
<!DOCTYPE html>
<html lang="en">
<head>
<meta charset="utf-8">
<title>KPW Holdings Group – Business Card</title>
<link rel="stylesheet" href="https://fonts.googleapis.com/css2?family=Open+Sans:wght@400;600;700&display=swap">
<style>
  :root {
    --page: #ffffff;
    --card-yellow: #ffcc00;
    --card-white: #ffffff;
    --ink: #333333;
    --logo-grey: #555555;
    --frame-line: #ffffff;
    --bar-purple: #8e3fa0;
    --bar-blue: #2f5fae;
    --bar-green: #4aa54a;
    --bar-orange: #ef7a22;
  }
  * { box-sizing: border-box; margin: 0; padding: 0; }
  html, body {
    width: 1200px;
    height: 1200px;
    overflow: hidden;
    background: var(--page);
    font-family: "Open Sans", Arial, sans-serif;
    color: var(--ink);
  }
  .business-card {
    position: absolute;
    left: 60px;
    top: 293px;
    width: 1080px;
    height: 615px;
    background: var(--card-yellow);
    box-shadow: 0 6px 24px rgba(0,0,0,0.12);
  }
  .card-shapes {
    position: absolute;
    inset: 0;
    width: 100%;
    height: 100%;
  }
  .brand {
    position: absolute;
    left: 117px;
    top: 68px;
    display: flex;
    align-items: center;
    gap: 16px;
  }
  .brand-square {
    width: 44px;
    height: 44px;
    background: var(--logo-grey);
  }
  .brand-name {
    font-size: 40px;
    font-weight: 600;
    color: var(--logo-grey);
    line-height: 1;
  }
  .service-line {
    position: absolute;
    left: 734px;
    top: 62px;
    font-size: 34px;
    line-height: 34px;
    color: var(--ink);
  }
  .service-line strong { font-weight: 700; }
  .person {
    position: absolute;
    left: 321px;
    top: 270px;
  }
  .person-name {
    font-size: 53px;
    line-height: 60px;
    color: var(--ink);
    font-weight: 400;
    white-space: nowrap;
  }
  .person-name strong { font-weight: 700; }
  .person-role {
    position: absolute;
    left: 433px;
    top: 60px;
    font-size: 32px;
    line-height: 36px;
    white-space: nowrap;
  }
  .contact {
    position: absolute;
    top: 478px;
    font-size: 29px;
    font-weight: 600;
    line-height: 36px;
    white-space: nowrap;
  }
  .contact-phone { left: 68px; }
  .contact-email { right: 48px; }
</style>
</head>
<body>
  <div class="business-card">
    <svg class="card-shapes" viewBox="0 0 1080 615" aria-hidden="true">
      <polygon class="brand-panel" points="0,0 632,0 572,173 0,173" fill="var(--card-white)"/>
      <g class="frame-lines" stroke="var(--frame-line)" stroke-width="4" fill="none">
        <line x1="19" y1="173" x2="19" y2="537"/>
        <line x1="36" y1="173" x2="36" y2="537"/>
        <line x1="619" y1="39" x2="1034" y2="39"/>
        <line x1="1034" y1="39" x2="1034" y2="537"/>
      </g>
      <line class="name-underline" x1="328" y1="355" x2="668" y2="355"
            stroke="var(--frame-line)" stroke-width="4" stroke-dasharray="58 14"/>
      <g class="colour-bar">
        <rect x="0" y="537" width="129" height="78" fill="var(--bar-purple)"/>
        <rect x="129" y="537" width="265" height="78" fill="var(--bar-blue)"/>
        <rect x="394" y="537" width="328" height="78" fill="var(--bar-green)"/>
        <rect x="722" y="537" width="358" height="78" fill="var(--bar-orange)"/>
      </g>
    </svg>

    <div class="brand">
      <span class="brand-square"></span>
      <span class="brand-name">KPW Holdings Group</span>
    </div>

    <p class="service-line"><strong>Business</strong><br>Management<br>Services.</p>

    <div class="person">
      <p class="person-name"><strong>Daniel</strong> Vesterby</p>
      <p class="person-role">Manager</p>
    </div>

    <p class="contact contact-phone">0472 915 603</p>
    <p class="contact contact-email">danielvesterby@kpwholdingsgroup.example</p>
  </div>
</body>
</html>
```